Business Card Design Project

Corvell Industrial Site Services Group would like to invite you to help us make our new business card design.

Industry/Entity Type

Business

```html
<!DOCTYPE html>
<html lang="en">
<head>
<meta charset="utf-8">
<title>Corvell Industrial – Business Card</title>
<link href="https://fonts.googleapis.com/css2?family=Oswald:wght@300;400;500&family=Questrial&display=swap" rel="stylesheet">
<style>
  :root {
    --page: #ffffff;
    --card-white: #ffffff;
    --ink-gray: #6d6e71;
    --tag-gray: #7a7b7e;
    --brand-green: #8dc63f;
    --green-deep: #76bd43;
    --green-light: #a6ce39;
    --on-green: #ffffff;
    --shadow: rgba(0, 0, 0, 0.28);
  }
  * { margin: 0; padding: 0; box-sizing: border-box; }
  html, body {
    width: 925px;
    height: 1200px;
    overflow: hidden;
    background: var(--page);
  }
  .sheet {
    position: relative;
    width: 925px;
    height: 1200px;
  }
  .card {
    position: absolute;
    left: 111px;
    width: 707px;
    height: 402px;
    box-shadow: 0 3px 14px var(--shadow);
  }
  .card--front {
    top: 111px;
    background: var(--card-white);
  }
  .card--back {
    top: 691px;
    background: linear-gradient(35deg, var(--green-deep) 0%, var(--brand-green) 45%, var(--green-light) 100%);
  }

  /* Front */
  .front-lockup {
    position: absolute;
    left: 0;
    right: 0;
    top: 130px;
    display: flex;
    flex-direction: column;
    align-items: center;
  }
  .front-name-row {
    display: flex;
    align-items: center;
    gap: 18px;
  }
  .front-mark {
    width: 46px;
    height: 46px;
    background: var(--brand-green);
  }
  .front-name {
    font-family: "Oswald", sans-serif;
    font-weight: 500;
    font-size: 56px;
    line-height: 1;
    letter-spacing: 0.5px;
    color: var(--ink-gray);
    white-space: nowrap;
  }
  .front-tagline {
    align-self: flex-end;
    margin-right: 58px;
    margin-top: 12px;
    font-family: "Oswald", sans-serif;
    font-weight: 300;
    font-size: 17px;
    letter-spacing: 3px;
    color: var(--tag-gray);
    white-space: nowrap;
  }

  /* Back */
  .back-lockup {
    position: absolute;
    left: 40px;
    top: 160px;
    display: flex;
    align-items: center;
    gap: 16px;
  }
  .back-mark {
    width: 62px;
    height: 62px;
    background: var(--on-green);
  }
  .back-name {
    font-family: "Oswald", sans-serif;
    font-weight: 500;
    font-size: 34px;
    line-height: 1.02;
    color: var(--on-green);
    white-space: nowrap;
  }
  .back-divider {
    position: absolute;
    left: 378px;
    top: 126px;
    width: 3px;
    height: 156px;
    background: var(--on-green);
  }
  .contact {
    position: absolute;
    left: 398px;
    top: 126px;
    color: var(--on-green);
    font-style: normal;
  }
  .contact-name {
    font-family: "Oswald", sans-serif;
    font-weight: 500;
    font-size: 24px;
    line-height: 1.1;
    margin-bottom: 2px;
  }
  .contact-line {
    font-family: "Questrial", sans-serif;
    font-size: 15.5px;
    line-height: 20px;
    white-space: nowrap;
  }
</style>
</head>
<body>
  <main class="sheet">
    <section class="card card--front" aria-label="Business card front">
      <div class="front-lockup">
        <div class="front-name-row">
          <span class="front-mark" aria-hidden="true"></span>
          <span class="front-name">CORVELL INDUSTRIAL</span>
        </div>
        <span class="front-tagline">SITE SERVICES GROUP</span>
      </div>
    </section>

    <section class="card card--back" aria-label="Business card back">
      <div class="back-lockup">
        <span class="back-mark" aria-hidden="true"></span>
        <span class="back-name">CORVELL<br>INDUSTRIAL</span>
      </div>
      <div class="back-divider"></div>
      <address class="contact">
        <div class="contact-name">DANA CORVELL</div>
        <div class="contact-line">4417 Ridgeline Ave</div>
        <div class="contact-line">Ashford Bay, Alberta</div>
        <div class="contact-line">T0K 2M4</div>
        <div class="contact-line">(780) 555-0142 Phone</div>
        <div class="contact-line">(780) 555-0187 Fax</div>
        <div class="contact-line">dcorvell@corvellindustrial.ca</div>
      </address>
    </section>
  </main>
</body>
</html>
```